Multifamily Property Needs a Flyer Design

I need a flyer that announces and highlights the renovations we are doing at an apartment community. The flyer needs to not only list the upgrades, but also communicate the renovation is an express upgrade. I've attached the color scheme we would like to use on the flyer (mustard and gray) and I've attached the property logo, Birch Hollowmere Apartments. Here are the renovations that are going to be done and more information that needs to be included on the flyer:Tagline: Now You See It, Now You Don’tLake Castleton renovation will soon be underway and ready for move-in by early November. We will be launching an Express Upgrade Service so that renovations will be completed in a blink of an eye. Contact the Leasing Office for more details, 555-302-7746. * All New Flooring* All New Kitchen, including New Countertops New Cabinets New Hardware New Appliances* New Designer Lighting and Plumbing Fixtures* New Bathroom Upgrades, including New Countertops New Cabinets New HardwareComing 2018:*New Dog Park*New Clubhouse*All New Pool Furniture and Accessories

```html
<!DOCTYPE html>
<html lang="en">
<head>
<meta charset="utf-8">
<title>Birch Hollowmere Renovations Flyer</title>
<link href="https://fonts.googleapis.com/css2?family=Alegreya+Sans:wght@400;500&display=swap" rel="stylesheet">
<style>
  :root {
    --gold: #c9982b;
    --gold-light: #d9ad3c;
    --gold-dark: #b4861f;
    --navy: #1b2a4c;
    --ink: #474747;
    --white: #ffffff;
  }
  * { margin: 0; padding: 0; box-sizing: border-box; }
  html, body { width: 946px; height: 1200px; overflow: hidden; background: #bfc0c2; }
  .flyer {
    position: relative;
    width: 946px; height: 1200px;
    background: var(--white);
    font-family: "Alegreya Sans", "Trebuchet MS", sans-serif;
    color: var(--ink);
    overflow: hidden;
  }
  .shapes { position: absolute; inset: 0; }
  .brand {
    position: absolute; left: 40px; top: 110px;
    display: flex; align-items: center; gap: 14px;
    font-size: 31px; font-weight: 500; letter-spacing: 1px;
    color: var(--navy);
  }
  .brand-dot { width: 26px; height: 26px; border-radius: 50%; background: var(--navy); }
  .headline {
    position: absolute; right: 40px; top: 30px;
    text-align: right; color: var(--white);
    font-size: 48px; font-weight: 400; line-height: 50px;
  }
  .intro {
    position: absolute; right: 74px; top: 259px; width: 340px;
    text-align: right; font-size: 18.5px; line-height: 25.5px;
  }
  .phone {
    position: absolute; right: 68px; top: 482px;
    display: flex; align-items: center; gap: 12px;
    font-size: 35px; color: var(--navy);
  }
  .phone svg { width: 42px; height: 42px; }
  .upgrade { position: absolute; left: 500px; }
  .upgrade-icon {
    position: absolute; left: 0; width: 78px; height: 54px;
    background: var(--gold); border: 3px solid var(--white);
    border-radius: 5px; box-shadow: 0 0 0 1px var(--gold);
  }
  .upgrade-icon svg { width: 100%; height: 100%; }
  .upgrade-text {
    position: absolute; left: 113px; width: 300px;
    font-size: 21.5px; line-height: 29px;
  }
  .upgrade-text ul { list-style: none; padding-left: 8px; }
  .upgrade-text li::before {
    content: ""; display: inline-block; width: 7px; height: 7px;
    border-radius: 50%; background: var(--gold);
    margin-right: 14px; vertical-align: middle;
  }
  .coming-tab {
    position: absolute; left: 0; width: 946px; top: 1068px;
    text-align: center; color: var(--white);
    font-size: 38px; line-height: 52px;
  }
  .amenities {
    position: absolute; left: 0; right: 0; top: 1141px;
    display: flex; justify-content: center; gap: 34px;
    color: var(--white); font-size: 23px; list-style: none;
  }
  .amenities li::before {
    content: ""; display: inline-block; width: 7px; height: 7px;
    border-radius: 50%; background: var(--white);
    margin-right: 12px; vertical-align: middle;
  }
</style>
</head>
<body>
<main class="flyer">
  <svg class="shapes" width="946" height="1200" viewBox="0 0 946 1200" aria-hidden="false">
    <defs>
      <linearGradient id="goldBand" x1="0" y1="0" x2="1" y2="0">
        <stop offset="0" stop-color="#e0b13a"/>
        <stop offset="1" stop-color="#b98a20"/>
      </linearGradient>
      <linearGradient id="kitchenTones" x1="0" y1="0" x2="1" y2="1">
        <stop offset="0" stop-color="#d9c7a0"/>
        <stop offset="0.45" stop-color="#8a5a34"/>
        <stop offset="0.75" stop-color="#9a9892"/>
        <stop offset="1" stop-color="#6b6864"/>
      </linearGradient>
    </defs>
    <!-- top right gold band -->
    <path d="M412,0 C395,70 372,130 338,170 C520,150 720,170 946,206 L946,0 Z" fill="url(#goldBand)"/>
    <!-- navy swoosh -->
    <path d="M330,178 C540,170 760,200 946,236 L946,252 C760,214 540,186 330,178 Z" fill="var(--navy)"/>
    <!-- kitchen photograph area -->
    <path role="img" aria-label="Photo of an apartment kitchen shown half before and half after renovation, wood cabinets, tan tile and gray plank flooring"
          d="M0,218 C120,190 240,176 338,178 C455,300 505,460 496,640 C488,820 474,960 472,1088 L0,1088 Z"
          fill="url(#kitchenTones)"/>
    <!-- navy edge along photo -->
    <path d="M338,178 C455,300 505,460 496,640 C488,820 474,960 472,1088 L488,1088 C490,960 504,820 512,640 C522,460 470,290 352,178 Z" fill="var(--navy)"/>
    <!-- bottom gold band and tab -->
    <rect x="0" y="1088" width="946" height="112" fill="var(--gold)"/>
    <path d="M300,1068 L646,1068 L672,1095 L646,1122 L300,1122 L274,1095 Z" fill="var(--navy)"/>
  </svg>

  <div class="brand"><span class="brand-dot"></span>BIRCH HOLLOWMERE</div>

  <h1 class="headline">Now You See It,<br>Soon You Won't.</h1>

  <p class="intro">Renovations at Birch Hollowmere will soon be underway. As part of this process, we are launching an Express Upgrades service where renovations will be done in the blink of an eye. Watch for more details and please feel free to contact the Leasing Office with any questions.</p>

  <div class="phone">555-302-7746
    <svg viewBox="0 0 42 42"><circle cx="21" cy="21" r="18.5" fill="none" stroke="var(--gold)" stroke-width="3"/><path d="M15,12 l4,0 l2,6 l-3,2 c1.5,3 3.5,5 6,6 l2,-3 l6,2 l0,4 c-9,1 -18,-8 -17,-17 z" fill="none" stroke="var(--gold)" stroke-width="2.2" stroke-linejoin="round"/></svg>
  </div>

  <section class="upgrade" style="top:0">
    <div class="upgrade-icon" style="top:572px"><svg viewBox="0 0 78 54"><path d="M16,14 h46 v26 h-46 z M16,27 h46 M31,14 v13 M47,14 v13 M24,27 v13 M39,27 v13 M54,27 v13" fill="none" stroke="#fff" stroke-width="2"/></svg></div>
    <div class="upgrade-text" style="top:581px">All New Flooring</div>

    <div class="upgrade-icon" style="top:636px"><svg viewBox="0 0 78 54"><path d="M18,30 h42 v14 h-42 z M39,30 v14 M30,22 h18 M39,22 v-8 h6" fill="none" stroke="#fff" stroke-width="2"/><circle cx="29" cy="37" r="2" fill="#fff"/><circle cx="49" cy="37" r="2" fill="#fff"/></svg></div>
    <div class="upgrade-text" style="top:640px">All New Kitchen, including
      <ul><li>New Countertops</li><li>New Cabinets</li><li>New Hardware</li><li>New Appliances</li></ul>
    </div>

    <div class="upgrade-icon" style="top:812px"><svg viewBox="0 0 78 54"><path d="M14,16 h50 M22,16 v12 M34,16 v12 M46,16 v12 M58,16 v12" fill="none" stroke="#fff" stroke-width="2"/><circle cx="22" cy="32" r="4" fill="#fff"/><circle cx="34" cy="32" r="4" fill="#fff"/><circle cx="46" cy="32" r="4" fill="#fff"/><circle cx="58" cy="32" r="4" fill="#fff"/></svg></div>
    <div class="upgrade-text" style="top:816px">New Designer Lighting and<br>Plumbing Fixtures</div>

    <div class="upgrade-icon" style="top:903px"><svg viewBox="0 0 78 54"><path d="M12,28 h34 v6 c0,6 -4,9 -10,9 h-14 c-6,0 -10,-3 -10,-9 z M18,28 v-12 h5 M54,30 h12 M60,30 v14 M54,44 h12" fill="none" stroke="#fff" stroke-width="2"/><circle cx="60" cy="18" r="6" fill="none" stroke="#fff" stroke-width="2"/></svg></div>
    <div class="upgrade-text" style="top:902px">New Bathroom Upgrades,<br>including
      <ul><li>New Countertops</li><li>New Cabinets</li><li>New Hardware</li></ul>
    </div>
  </section>

  <div class="coming-tab">Coming 2018</div>

  <ul class="amenities">
    <li>New Dog Park</li>
    <li>Redesigned Clubhouse</li>
    <li>All New Pool Furniture and Accessories</li>
  </ul>
</main>
</body>
</html>
```